Dermatology Office Business Card Update

Updating some information on the current business card. Do not adjust font type. Need both rounded rectangle and rounded square card files. In addition, must have separate file for both rectangle and square cards for gold foil printing.1. Update phone number with: 555-318-27602. Remove email address3. Add this website to be listed under quillbrookdermatology.example:jilluxe.com4. Under updated phone number, add the flickvue logo in color and then a space and the following text: @dermjill5. Gold foil should be inclusive of the outline of the butterfly wings on the front. Also should put a small hyphen that is also gold foil under the cursive Nora Belcastro, MD and before the block lettering begins.Back of card remains the samePlease feel free to contact me with any questions!

Target Market(s)

Patients

Contact Information for Business Card

Just needs some updates along with files for gold foil printing

Requirements
Must have
• Updating some information on the current business card. Do not adjust font type. Need both rounded rectangle and rounded square card files. In addition, must have separate file for both rectangle and square cards for gold foil printing.
• 1. Update phone number with: 555-318-2760
• 2. Remove email address
• 3. Add this website to be listed under quillbrookdermatology.example:
• norvatek.example
• 4. Under updated phone number, add the flickvue logo in color and then a space and the following text: @docnorabel
• 5. Gold foil should be inclusive of the outline of the butterfly wings on the front. Also should put a small hyphen that is also gold foil under the cursive Nora Belcastro, MD and before the block lettering begins.
• Back of card remains the same
• Please feel free to contact me with any questions!

```html
<!DOCTYPE html>
<html lang="en">
<head>
<meta charset="utf-8">
<title>Quillbrook Dermatology – Business Card</title>
<link rel="stylesheet" href="https://fonts.googleapis.com/css2?family=Lexend:wght@400;500;600&family=Montserrat:wght@500&family=Arimo:wght@400&display=swap">
<style>
  :root {
    --navy: #33435f;
    --rose: #c3949a;
    --gold: #e1c67a;
    --gold-deep: #b08c3e;
    --mauve: #8d6c86;
    --band-navy: #22416a;
    --band-rose: #b88890;
    --white: #ffffff;
    --border: #2b2b2b;
  }
  * { margin: 0; padding: 0; box-sizing: border-box; }
  html, body { width: 1027px; height: 1200px; overflow: hidden; background: var(--white); }
  body { position: relative; }

  .card { position: absolute; left: 74px; width: 880px; }

  /* Front */
  .card-front { top: 68px; height: 491px; border: 1px solid var(--border); background: var(--white); overflow: hidden; }
  .brand-mark {
    position: absolute; left: 50%; top: 70px; width: 58px; height: 58px;
    margin-left: -29px; border-radius: 50%; background: var(--rose);
  }
  .brand-name {
    position: absolute; left: 0; right: 0; top: 160px; text-align: center;
    font-family: "Lexend", sans-serif; font-weight: 500; color: var(--navy);
    font-size: 24px; line-height: 28px; letter-spacing: 0.3em; text-indent: 0.3em;
  }
  .brand-rule { position: absolute; left: 311px; top: 256px; width: 255px; height: 2px; background: var(--gold); }

  .doctor-name {
    position: absolute; left: 104px; top: 309px; line-height: 32px;
    font-family: "Montserrat", sans-serif; font-weight: 500; font-size: 25px;
    letter-spacing: 0.2em; color: var(--navy); white-space: nowrap;
  }
  .doctor-name .credential { color: var(--rose); }
  .divider {
    position: absolute; left: 504px; top: 300px; width: 3px; height: 47px;
    background: linear-gradient(var(--gold), var(--gold-deep));
  }
  .phone {
    position: absolute; left: 541px; top: 306px; line-height: 36px;
    font-family: "Lexend", sans-serif; font-weight: 600; font-size: 30px;
    color: var(--navy); letter-spacing: 0.01em; white-space: nowrap;
  }
  .phone .dash { color: var(--rose); }
  .social {
    position: absolute; left: 542px; top: 345px; display: flex; align-items: center; gap: 10px;
    font-family: "Arimo", sans-serif; font-size: 23px; color: var(--rose); white-space: nowrap;
  }
  .social-square { width: 14px; height: 14px; background: var(--rose); }
  .websites {
    position: absolute; left: 0; right: 0; top: 455px; text-align: center; color: var(--rose);
  }
  .website-primary {
    position: absolute; left: 0; right: 0; top: -64px;
    font-family: "Lexend", sans-serif; font-size: 25px; letter-spacing: 0.06em; line-height: 30px;
  }
  .website-secondary {
    position: absolute; left: 0; right: 0; top: -33px;
    font-family: "Arimo", sans-serif; font-size: 24px; line-height: 28px;
  }
  .front-band {
    position: absolute; left: 0; right: 0; bottom: 0; height: 41px;
    background: linear-gradient(90deg, var(--band-navy) 0%, var(--mauve) 30%, var(--band-rose) 70%, #b4868d 100%);
  }

  /* Back */
  .card-back {
    top: 642px; height: 490px; overflow: hidden;
    background:
      radial-gradient(ellipse at 100% 100%, #23406a 0%, rgba(35,64,106,0) 38%),
      radial-gradient(ellipse at 0% 0%, #c19aa1 0%, rgba(193,154,161,0) 45%),
      linear-gradient(135deg, #b3848f 0%, #9a6a77 45%, #7f607b 75%, #4c5275 100%);
  }
  .back-wordmark {
    position: absolute; left: 0; right: 0; top: 200px; text-align: center;
    font-family: "Lexend", sans-serif; font-weight: 500; font-size: 34px;
    letter-spacing: 0.3em; text-indent: 0.3em; color: var(--white);
  }
  .tagline {
    position: absolute; left: 0; right: 0; top: 345px; text-align: center;
    font-family: "Montserrat", sans-serif; font-weight: 500; font-size: 20px;
    letter-spacing: 0.3em; text-indent: 0.3em; color: var(--white);
  }
</style>
</head>
<body>
  <section class="card card-front" aria-label="Business card front">
    <div class="brand-mark"></div>
    <div class="brand-name">QUILLBROOK<br>DERMATOLOGY</div>
    <div class="brand-rule"></div>

    <div class="doctor-name">NORA BELCASTRO, <span class="credential">MD</span></div>
    <div class="divider"></div>
    <div class="phone">555<span class="dash">-</span>318<span class="dash">-</span>2760</div>
    <div class="social"><span class="social-square"></span><span>flickvue</span><span>@docnorabel</span></div>

    <div class="websites">
      <div class="website-primary">quillbrookdermatology.example</div>
      <div class="website-secondary">norvatek.example</div>
    </div>
    <div class="front-band" role="img" aria-label="Watercolour band fading from navy to dusty rose"></div>
  </section>

  <section class="card card-back" role="img" aria-label="Dusty rose and navy watercolour texture background">
    <div class="back-wordmark">QUILLBROOK</div>
    <div class="tagline">BECOMING YOU</div>
  </section>
</body>
</html>
```